Website design needed for Renewable utilities company based in New Zealand.

Website design needed for Tarnwick Collective based in New Zealand.

Please see attached logo.

We sell solar panels, vertical axis wind turbines, atmospheric water generators and other related equipment for those who don't have access or don't want to depend on the government, city councils for their utilities (power and water).

We like metallic texture, dark grey and purple, red or blue colours. The design should go well with the attached logo.

Target Market(s)

The Eco conscious

Industry/Entity Type

Government

Logo Text

Tarnwick Horizon

Requirements
Must have
• Must Have:
- Metallic finish is a must.
- Design should fit around the attached logo well.
Nice to have
• Sharpe design prefred rather than rounded edges

```html
<!DOCTYPE html>
<html lang="en">
<head>
<meta charset="utf-8">
<title>Tarnwick Horizon — Renewable Utilities</title>
<link rel="stylesheet" href="https://fonts.googleapis.com/css2?family=Open+Sans:wght@400;600&family=Arimo:wght@400&display=swap">
<style>
:root{
  --bar-dark:#3a3a3a;
  --bar-mid:#555;
  --header-top:#e4e4e4;
  --header-bottom:#b9b9b9;
  --brand-blue:#1f6fa8;
  --nav-grey:#8a8a8a;
  --nav-active:#2b7fb0;
  --section-top:#d6d6d6;
  --section-bottom:#c3c3c3;
  --highlight:#a4b5bf;
  --heading-blue:#2a7ba3;
  --body-text:#3f3f3f;
  --orange-top:#f6a53f;
  --orange-bottom:#d9771a;
  --frame:#9c9c9c;
  --footer-text:#d0d0d0;
  --footer-head:#2aa0d6;
}
*{box-sizing:border-box;margin:0;padding:0}
html,body{width:862px;height:1200px;overflow:hidden}
body{position:relative;font-family:"Arimo",Arial,sans-serif;background:var(--section-bottom)}
.abs{position:absolute}

.topbar{left:0;top:0;width:862px;height:29px;background:linear-gradient(var(--bar-mid),var(--bar-dark))}
.topbar .phone{right:36px;top:6px;color:#eee;font:400 14px "Open Sans",sans-serif;display:flex;align-items:center;gap:8px}

.site-header{left:0;top:29px;width:862px;height:125px;background:linear-gradient(var(--header-top),var(--header-bottom))}
.brand{left:76px;top:20px;width:150px;text-align:center}
.brand .mark{width:52px;height:52px;border-radius:50%;background:var(--brand-blue);margin:0 auto 6px}
.brand .name{font:400 18px "Open Sans",sans-serif;color:var(--brand-blue);white-space:nowrap}

.main-nav{left:391px;top:14px;height:92px;display:flex}
.main-nav .item{height:92px;border-left:1px solid #a9a9a9;box-shadow:inset 1px 0 #eee;display:flex;flex-direction:column;align-items:center;justify-content:flex-end;padding-bottom:12px;font:400 14px "Open Sans",sans-serif;color:var(--nav-grey);gap:8px;white-space:nowrap}
.main-nav .item:last-child{border-right:1px solid #a9a9a9}
.main-nav .item.active{color:var(--nav-active)}

.hero{left:0;top:154px;width:862px;height:316px;overflow:hidden}
.hero .photo{left:0;top:0;width:862px;height:316px;background:linear-gradient(160deg,#4d6a86 0%,#34475c 55%,#5a4a44 100%)}
.hero svg.panel{left:0;top:0}
.hero .copy{left:665px;top:70px;width:175px;color:#fff}
.hero h1{font:400 18px "Open Sans",sans-serif;padding-bottom:6px;border-bottom:1px solid rgba(255,255,255,.5);margin-bottom:9px}
.hero p{font-size:11px;line-height:17px;text-align:justify}
.btn{display:inline-block;background:linear-gradient(var(--orange-top),var(--orange-bottom));color:#fff;border:1px solid #c86a12;border-radius:3px;text-align:center}
.hero .btn{margin-top:12px;width:105px;height:27px;line-height:25px;font-size:11px}
.dots{left:322px;top:300px;display:flex;gap:3px}
.dots span{width:11px;height:11px;border-radius:50%;border:2px solid #1f4f6a;background:#fff}
.dots span:first-child{background:#1f4f6a}

.products{left:0;top:470px;width:862px;height:369px;background:linear-gradient(var(--section-top),var(--section-bottom))}
.products .highlight{left:304px;top:24px;width:238px;height:310px;background:var(--highlight)}
.product{top:45px;width:186px}
.product h2{font:400 13px "Arimo",sans-serif;color:var(--heading-blue);text-align:center;white-space:nowrap;margin-bottom:10px}
.product .shot{width:186px;height:155px;border:5px solid var(--frame)}
.product p{margin-top:14px;font-size:10.2px;line-height:15px;color:var(--body-text)}
.product .btn{display:block;margin:6px 8px 0 auto;width:70px;height:18px;line-height:16px;font-size:9.5px}

.about{left:0;top:839px;width:862px;height:232px;background:linear-gradient(#cfcfcf,#a9a9a9)}
.about .rule{top:28px;height:4px;border-top:1px solid #999;border-bottom:1px solid #999}
.about h2{left:0;width:862px;top:17px;text-align:center;font:400 19px "Open Sans",sans-serif;color:var(--heading-blue)}
.about h2 span{color:#333}
.about .logo-box{left:98px;top:52px;width:153px;height:153px;border:5px solid #9a9a9a;background:#fff;display:flex;flex-direction:column;align-items:center;justify-content:center;gap:8px}
.about .logo-box .mark{width:48px;height:48px;border-radius:50%;background:var(--brand-blue)}
.about .logo-box .name{font:400 15px "Open Sans",sans-serif;color:var(--brand-blue)}
.about .text{left:269px;top:66px;width:490px;font-size:11px;line-height:17px;color:var(--body-text)}
.about .text p+p{margin-top:17px}

.site-footer{left:0;top:1071px;width:862px;height:129px;background:repeating-linear-gradient(0deg,#2e2e2e 0 2px,#363636 2px 4px)}
.site-footer h3{font:400 14px "Open Sans",sans-serif;letter-spacing:3px;color:var(--footer-head);margin-bottom:5px}
.site-footer ul{list-style:none}
.site-footer li{font:400 10px "Open Sans",sans-serif;color:var(--footer-text);height:18px;display:flex;align-items:center;gap:5px}
.site-footer li::before{content:"";width:5px;height:5px;border-top:2px solid var(--footer-head);border-right:2px solid var(--footer-head);transform:rotate(45deg)}
.col{top:14px}
.social{display:flex;gap:10px;margin:8px 0 0 2px}
.social span{width:26px;height:26px;border-radius:50%;background:#f0f0f0;border:2px solid #bbb}
.copyright{font:400 10.5px "Open Sans",sans-serif;color:var(--footer-text);margin-top:18px;margin-left:-10px}
</style>
</head>
<body>

<div class="abs topbar">
  <div class="abs phone">
    <svg width="18" height="12" viewBox="0 0 18 12"><path d="M1 4 Q9 -2 17 4 L15 6 L12 4.5 L12 3 Q9 2 6 3 L6 4.5 L3 6Z M4 7 H14 V11 H4Z" fill="#ddd"/></svg>
    Call us: 1800-555-0199
  </div>
</div>

<header class="abs site-header">
  <div class="abs brand"><div class="mark"></div><div class="name">Tarnwick Horizon</div></div>
  <nav class="abs main-nav">
    <div class="item active" style="width:81px">
      <svg width="40" height="38" viewBox="0 0 40 38"><path d="M20 2 L38 18 H33 V36 H24 V25 H16 V36 H7 V18 H2Z" fill="#2b7fb0"/></svg>Home</div>
    <div class="item" style="width:114px">
      <svg width="48" height="32" viewBox="0 0 48 32"><circle cx="12" cy="10" r="5" fill="#888"/><circle cx="36" cy="10" r="5" fill="#888"/><circle cx="24" cy="8" r="6" fill="#999"/><path d="M3 28 Q12 14 21 28Z M27 28 Q36 14 45 28Z M13 30 Q24 12 35 30Z" fill="#999"/></svg>Who we are</div>
    <div class="item" style="width:131px">
      <svg width="32" height="32" viewBox="0 0 32 32"><rect y="2" width="32" height="7" fill="#999"/><rect y="13" width="32" height="7" fill="#999"/><rect y="24" width="32" height="7" fill="#999"/></svg>What we Offer</div>
    <div class="item" style="width:114px">
      <svg width="46" height="28" viewBox="0 0 46 28"><rect x="1" y="1" width="44" height="26" fill="#aaa" stroke="#888"/><path d="M1 1 L23 17 L45 1" fill="none" stroke="#777" stroke-width="2"/></svg>Contact us</div>
  </nav>
</header>

<section class="abs hero">
  <div class="abs photo" role="img" aria-label="Photo: rows of solar panels in an open field"></div>
  <svg class="abs panel" width="862" height="316" viewBox="0 0 862 316">
    <defs><linearGradient id="pg" x1="0" y1="0" x2="0" y2="1"><stop offset="0" stop-color="#6fa3bd"/><stop offset="1" stop-color="#235a78"/></linearGradient></defs>
    <path d="M555 316 C650 250 680 100 650 0 H862 V316Z" fill="url(#pg)"/>
  </svg>
  <div class="abs copy">
    <h1>Lorem Ipsum text</h1>
    <p>Lorem ipsum dolor sit amet, consectetur adipiscing elit. Nullam mi augue, facilisis a quam sit amet, viverra interdum ligula. Cras fermentum cursus tellus, a dignissim metus cursus vel. dignissim convallis urna, eget tincidunt elit porta vitae.</p>
    <span class="btn">VIEW PRODUCT</span>
  </div>
  <div class="abs dots"><span></span><span></span><span></span><span></span></div>
</section>

<section class="abs products">
  <div class="abs highlight"></div>
  <article class="abs product" style="left:91px">
    <h2>SOLAR PANEL PRODUCTS</h2>
    <div class="shot" role="img" aria-label="Photo: single solar panel" style="background:linear-gradient(135deg,#c9d3e6,#5a76bd 60%,#3a4f9a)"></div>
    <p>Lorem ipsum dolor sit amet, consectetur adipiscing elit. Nullam mi augue, facilisis a quam sit amet, viverra interdum ligula. Cras fermentum.</p>
    <span class="btn">Read more</span>
  </article>
  <article class="abs product" style="left:328px">
    <h2>VERTICAL AXIS WIND TURBINE</h2>
    <div class="shot" role="img" aria-label="Photo: vertical axis wind turbines" style="background:linear-gradient(#2a5ca8,#6a92c8)"></div>
    <p>Lorem ipsum dolor sit amet, consectetur adipiscing elit. Nullam mi augue, facilisis a quam sit amet, viverra interdum ligula. Cras fermentum.</p>
    <span class="btn">Read more</span>
  </article>
  <article class="abs product" style="left:576px">
    <h2>ATMOSPHERIC WATER GEN.</h2>
    <div class="shot" role="img" aria-label="Photo: atmospheric water generator units" style="background:linear-gradient(160deg,#2f5f8e,#1d3f66)"></div>
    <p>Lorem ipsum dolor sit amet, consectetur adipiscing elit. Nullam mi augue, facilisis a quam sit amet, viverra interdum ligula. Cras fermentum.</p>
    <span class="btn">Read more</span>
  </article>
</section>

<section class="abs about">
  <div class="abs rule" style="left:62px;width:298px"></div>
  <div class="abs rule" style="left:492px;width:312px"></div>
  <h2 class="abs">About <span>Us</span></h2>
  <div class="abs logo-box"><div class="mark"></div><div class="name">Tarnwick Horizon</div></div>
  <div class="abs text">
    <p>Lorem ipsum dolor sit amet, consectetur adipiscing elit. Nullam mi augue, facilisis a quam sit amet, viverra interdum ligula. Cras fermentum cursus tellus, a dignissim metus cursus vel. Nulla non leo pellentesque, varius neque et, porta velit. Fusce fringilla sodales magna non mattis. Nunc tempus dignissim erat vitae tincidunt. Nulla eget laoreet turpis.</p>
    <p>Sed quis augue mi. In dignissim convallis urna, eget tincidunt elit porta vitae. Etiam ut eros rutrum, iaculis erat sit amet, condimentum orci. Duis interdum ipsum eget purus varius, vitae fermentum ligula pellentesque.</p>
  </div>
</section>

<footer class="abs site-footer">
  <div class="abs col" style="left:131px">
    <h3>QUICKLINKS</h3>
    <ul><li>Home</li><li>Who we are</li><li>What we Offer</li><li>Contact us</li></ul>
  </div>
  <div class="abs col" style="left:366px">
    <h3>USEFUL LINKS</h3>
    <ul><li>FAQ</li><li>Customer Service</li><li>Product Warranty</li><li>Sitemap</li></ul>
  </div>
  <div class="abs col" style="left:601px">
    <h3>SOCIAL MEDIA</h3>
    <div class="social" aria-label="Social media links"><span></span><span></span><span></span><span></span></div>
    <div class="copyright">Copyright 2013 · All rights reserved</div>
  </div>
</footer>

</body>
</html>
```